New Corporate Business Card - Velmorana

What we need:
We need a new corporate business card.
We want a new template that we can change by ourself.
We want business card modern and minimalist but that looks professional.
We will print it in 300 gr soft-touch.
Why not a white side with the logo and a red/grey side with the content?
Why not a grey side and a red side like our logo?
I am sure that you have better idea than ours that's the reason we come here.

Who we are:
We are a private label company in cosmetics based in Switzerland. We work in BtoB. We make skin care products for other brands.

Target Market(s)

B to B - Worldwide - any gender

Industry/Entity Type

Cosmetics

Contact Information for Business Card

Side 1:
Logo
Your Swiss Private Label Manufacturer or www.velmorana-example.ch

Side 2:
Name and surname (Example: Lucien Marchetaz)
Job Description (General Manager)
Telephone (+41 32 915 63 00)
Direct (+41 32 915 63 63)
Email (lucien.marchetaz@velmorana-example.ch)
Chemin des Pélerines 14, 2000 Neuchâtel, Switzerland
www.velmorana-example.ch

Font styles to use
Serif
Sans Serif

Requirements
Must have
• You can use 4 colors: white, red, grey and/or black .
Should not have
• Too much colors, too much things. We want it simple!

```html
<!DOCTYPE html>
<html lang="en">
<head>
<meta charset="utf-8">
<title>Velmorana – Business Card</title>
<link href="https://fonts.googleapis.com/css2?family=Lato:wght@400;700&display=swap" rel="stylesheet">
<style>
  :root {
    --backdrop: #262626;
    --card: #1b1b1b;
    --red: #e01b1b;
    --white: #f4f4f4;
    --grey: #a7a8aa;
  }
  * { box-sizing: border-box; margin: 0; padding: 0; }
  html, body { width: 1200px; height: 900px; overflow: hidden; }
  body {
    background: var(--backdrop);
    font-family: "Lato", sans-serif;
    position: relative;
  }
  .card {
    position: absolute;
    left: 300px;
    width: 600px;
    height: 360px;
    background: var(--card);
    box-shadow: 0 6px 18px rgba(0,0,0,.45);
  }
  .card--front { top: 70px; }
  .card--back { top: 470px; }

  .brand {
    display: flex;
    align-items: center;
    gap: 12px;
  }
  .brand__square {
    width: 18px;
    height: 18px;
    background: var(--red);
  }
  .brand__name {
    font-weight: 700;
    color: var(--white);
    letter-spacing: 0.18em;
    text-transform: uppercase;
  }
  .card--front .brand {
    position: absolute;
    top: 50%;
    left: 50%;
    transform: translate(-50%, -50%);
  }
  .card--front .brand__name { font-size: 30px; }

  .card--back .brand {
    position: absolute;
    left: 40px;
    top: 50%;
    transform: translateY(-50%);
  }
  .card--back .brand__name { font-size: 22px; }
  .card--back .brand__square { width: 14px; height: 14px; }

  .contact {
    position: absolute;
    left: 290px;
    top: 86px;
    color: var(--white);
  }
  .contact__name {
    color: var(--red);
    font-weight: 700;
    font-size: 21px;
    letter-spacing: 0.06em;
  }
  .contact__role {
    font-size: 14px;
    margin-top: 2px;
    letter-spacing: 0.03em;
  }
  .contact__address {
    font-size: 14px;
    line-height: 1.4;
    margin-top: 14px;
    font-style: normal;
  }
  .contact__lines {
    list-style: none;
    margin-top: 12px;
    font-size: 14px;
    line-height: 1.45;
  }
  .contact__lines li {
    display: flex;
    align-items: center;
    gap: 8px;
  }
  .contact__lines svg {
    width: 11px;
    height: 11px;
    flex: none;
    fill: none;
    stroke: var(--red);
    stroke-width: 2;
  }
  .accent { color: var(--red); }
</style>
</head>
<body>

  <section class="card card--front" aria-label="Business card front">
    <div class="brand">
      <span class="brand__square"></span>
      <span class="brand__name">Velmorana</span>
    </div>
  </section>

  <section class="card card--back" aria-label="Business card back">
    <div class="brand">
      <span class="brand__square"></span>
      <span class="brand__name">Velmorana</span>
    </div>

    <div class="contact">
      <h1 class="contact__name">Lucien Marchetaz</h1>
      <p class="contact__role">General Manager</p>
      <address class="contact__address">
        Chemin des Pélerines 14,<br>
        2000 Neuchâtel, Switzerland
      </address>
      <ul class="contact__lines">
        <li>
          <svg viewBox="0 0 12 12"><path d="M2 1.5 L4.5 1.5 L5 4 L3.6 5 Q4.8 7.4 7 8.4 L8 7 L10.5 7.5 L10.5 10 Q5.5 10.5 1.8 4.2 Z"/></svg>
          (+41 32 915 63 00)
        </li>
        <li>
          <svg viewBox="0 0 12 12"><rect x="3" y="1" width="6" height="10" rx="1"/><line x1="5" y1="9" x2="7" y2="9"/></svg>
          (+41 32 915 63 63)
        </li>
        <li>
          <svg viewBox="0 0 12 12"><circle cx="6" cy="6" r="4.8"/><ellipse cx="6" cy="6" rx="2" ry="4.8"/><line x1="1.2" y1="6" x2="10.8" y2="6"/></svg>
          <span>www.<span class="accent">velmorana-example</span>.ch</span>
        </li>
        <li>
          <svg viewBox="0 0 12 12"><rect x="1" y="2.5" width="10" height="7"/><path d="M1 2.5 L6 6.5 L11 2.5"/></svg>
          lucien.marchetaz@velmorana-example.ch
        </li>
      </ul>
    </div>
  </section>

</body>
</html>
```